[Raw Food + Juice Bar] Digital Menu Boards (2)

We need designs for our digital menu screens. Dimensions are 1080 x 1920 (9:16). Screens are in portrait mode–2 of them. They will be side by side so designs should be cohesive. We'll need the (Adobe) source files to be able to easily edit in the future.

Check out our Instagram (@pulpvia) to see current brand imagery for inspiration. Please disregard our current website design as it shows our old branding. Visit our Brightlistr page to get a feel of the store flow in which the menu boards will be displayed: https://www.brightlistr.com/biz/pulpvia-chicago-6

See "Larchmere Menu" attachment for content that will be incorporated into the design for 2 screens.

See "Cleanse Brochure" attachment to see current material we are using to promote our cleansing program. We would like to designate a portion of our menu to promote cleanse options, depending on how much room is available.

Also attached is a photo of our current, static menu board.

We've attached photos of color palettes we like.

Target Market(s)

Health-conscious individuals, healthy moms, fitness gurus, professionals

Industry/Entity Type

Health And Wellness

Font styles to use
Serif
Sans Serif

Colors

Designer to choose colors to be used in the design.

Requirements
Must have
• We need designs for our digital menu screens. Dimensions are 1080 x 1920 (9:16). Screens are in portrait mode–2 of them. We'll need the (Adobe) source files to be able to easily edit in the future. To ensure the sizing of the outputted file is correct and spaced correctly, send us a test file to test on our TV.
Nice to have
• Ideally, the menu will reflect current branding with font usage of one or more of the following:
• FuturaStd-Bold
• Desiderata-Regular
• Wisdom Script
• Bernier Typeface
• Swistblnk Banthers
• Hanley
• If there is space, we'd like to have space to roll a photo/video slideshow on the menu.

```html
<!DOCTYPE html>
<html lang="en">
<head>
<meta charset="utf-8">
<title>Smoothies Menu Board</title>
<link href="https://fonts.googleapis.com/css2?family=Pacifico&family=Oswald:wght@500;600&family=Roboto+Condensed:wght@700&display=swap" rel="stylesheet">
<style>
  :root {
    --teal: #0fa39d;
    --teal-dark: #0b8c88;
    --leaf: #c4e09c;
    --leaf-text: #ffffff;
    --price: #f4ea4e;
    --copy: #ffffff;
    --ink: #1d2a2a;
    --photo-a: #6f8c3e;
    --photo-b: #a37a4e;
  }
  * { margin: 0; padding: 0; box-sizing: border-box; }
  html, body { width: 674px; height: 1200px; overflow: hidden; }
  body { background: var(--teal); position: relative; font-family: "Roboto Condensed", sans-serif; }

  .board-title {
    position: absolute; left: 246px; top: 6px;
    color: #fff; font-family: "Pacifico", cursive; font-size: 50px; line-height: 1.3;
  }
  .board-title .size {
    font-family: "Oswald", sans-serif; font-size: 26px; font-weight: 500; margin-left: 4px;
  }

  .hero-photo {
    position: absolute; left: 0; top: 96px; width: 258px; height: 846px;
    background: linear-gradient(160deg, var(--photo-b) 0%, #8a6a45 35%, var(--photo-a) 60%, #9c7a52 100%);
  }

  .menu-item { position: absolute; left: 286px; width: 370px; }
  .item-head { display: flex; align-items: center; gap: 10px; margin-bottom: 10px; }
  .item-name {
    background: var(--leaf); color: var(--leaf-text);
    font-family: "Oswald", sans-serif; font-weight: 600; font-size: 19px; letter-spacing: 1px;
    padding: 0 6px; line-height: 28px; text-transform: uppercase;
  }
  .item-price { color: var(--price); font-family: "Oswald", sans-serif; font-weight: 500; font-size: 20px; }
  .item-desc {
    color: var(--copy); font-size: 11px; line-height: 19px; text-transform: uppercase; letter-spacing: 0.2px;
  }

  .build-panel {
    position: absolute; left: 70px; top: 970px; width: 552px; height: 212px;
    background: var(--leaf); padding: 12px 14px;
  }
  .build-title { font-family: "Pacifico", cursive; color: var(--teal-dark); font-size: 24px; line-height: 1.4; }
  .build-title .price { font-family: "Oswald", sans-serif; color: #fff; font-size: 24px; font-weight: 500; }
  .build-steps { list-style: none; margin-top: 8px; }
  .build-steps li {
    font-size: 11px; line-height: 23px; color: var(--ink); text-transform: uppercase;
    padding-left: 38px; text-indent: -38px;
  }
  .build-steps li span { color: #fff; }
  .build-steps li.wrap { line-height: 20px; margin-bottom: 3px; }
</style>
</head>
<body>
  <h1 class="board-title">Smoothies<span class="size">(18oz)</span></h1>

  <div class="hero-photo" role="img" aria-label="Photo of a green cold-pressed juice bottle lying on pine needles and bark"></div>

  <section class="menu-item" style="top:101px">
    <div class="item-head"><span class="item-name">Black Phoenix</span><span class="item-price">10.5</span></div>
    <p class="item-desc">Housemade almond milk, cold brew coffee, banana, coconut meat, raw cacao, medjool dates, tocotrienols, maca, topped with raw cacao drizzle and housemade coconut whip.</p>
  </section>

  <section class="menu-item" style="top:224px">
    <div class="item-head"><span class="item-name">Green Magnolia</span><span class="item-price">11</span></div>
    <p class="item-desc">Housemade almond milk, banana, avocado, spinach, sprouted almond butter, vitaleaf greens, maca, moringa, medjool dates, tocotrienols.</p>
  </section>

  <section class="menu-item" style="top:356px">
    <div class="item-head"><span class="item-name">Green Tie Ball</span><span class="item-price">10</span></div>
    <p class="item-desc">Housemade almond milk, banana, avocado, pineapple, spinach, matcha, spirulina, mint, tocotrienols, local honey, pink salt (upgrade: vitaleaf greens, +1).</p>
  </section>

  <section class="menu-item" style="top:490px">
    <div class="item-head"><span class="item-name">Old World Order</span><span class="item-price">10</span></div>
    <p class="item-desc">Housemade almond milk, banana, blueberries, peanut butter, medjool dates, tocotrienols, lucuma, pink salt.</p>
  </section>

  <section class="menu-item" style="top:593px">
    <div class="item-head"><span class="item-name">Macro Maca Protein</span><span class="item-price">10.5</span></div>
    <p class="item-desc">Fresh-cracked coconut water, cherries, banana, peanut butter, vegan mocha protein powder, maca.</p>
  </section>

  <section class="menu-item" style="top:703px">
    <div class="item-head"><span class="item-name">Fire Brigade</span><span class="item-price">10</span></div>
    <p class="item-desc">Fresh-cracked coconut water, apple juice, coconut meat, banana, mango, pineapple, strawberry, tocotrienols, camu camu, hemp seeds, jalapeno.</p>
  </section>

  <section class="menu-item" style="top:836px">
    <div class="item-head"><span class="item-name">Winter Peppermint</span><span class="item-price">10.5 *SEASONAL*</span></div>
    <p class="item-desc">Almond milk, banana, cherries, raw cacao drizzle, sprouted almond butter, tocotrienols, dates, peppermint, pink salt topped with raw cacao drizzle, cacao nibs, mint and housemade coconut whip.</p>
  </section>

  <section class="build-panel">
    <h2 class="build-title">Build Your Own Smoothie <span class="price">- 10.5</span></h2>
    <ol class="build-steps">
      <li class="wrap"><span>Step 1:</span> Start with your liquid: housemade almond milk, apple juice, or coconut water</li>
      <li><span>Step 2:</span> Add your base: avocado, banana, or coconut meat</li>
      <li><span>Step 3:</span> Choose up to 3 fruits/ veggies</li>
      <li><span>Step 4:</span> Choose up to 2 superfoods</li>
      <li><span>Step 5:</span> Choose a sweetener (medjool dates, local honey, xylitol)</li>
    </ol>
  </section>
</body>
</html>
```